Stylish business cards for KX7

To create an appealing and professional business card design for a WOMEN Owned Construction Supply Company.
2 sided card. Incorporate brand elements, curvy, colorful, sleek and bright. No solid white background. attached samples of styles added shapes/ribbons. Want something with that WOW that looks awesome, factor. It is a new logo, so feel free to mess with logo colors in the blue and teal factors that can look good with both dark and light background. If you want to try a watermark with just the KX7, without the "Supply" that might look cool to.

Industry/Entity Type

Women owned construction supply company

Contact Information for Business Card

Name, Title, and phone number and email, web page. maybe spot for qr code.

Font styles to use
Sans Serif

Requirements
Nice to have
• would love to see colors, maybe stylish ribbon dividers or some sort of 2 or 3 tone color card that compliments logo.
Should not have
• Please do not have all white background. Do not include Home/reale state/ or building images.

```html
<!DOCTYPE html>
<html lang="en">
<head>
<meta charset="UTF-8">
<title>KX7 Supply – Business Cards</title>
<link rel="stylesheet" href="https://fonts.googleapis.com/css2?family=Poppins:wght@400;500;600&display=swap">
<style>
  :root {
    --canvas-bg: #2b2b2d;
    --front-bg: #6e8197;
    --front-ink: #e4e9ef;
    --back-bg-top: #f4f8fb;
    --back-bg-bottom: #e3eef5;
    --navy: #1f3a5c;
    --teal: #2a9fc4;
    --teal-soft: #8fd0e4;
    --body-ink: #2f3540;
    --divider: #7d8ea3;
  }
  * { box-sizing: border-box; margin: 0; padding: 0; }
  html, body {
    width: 1200px; height: 875px; overflow: hidden;
    background: var(--canvas-bg);
    font-family: "Poppins", sans-serif;
  }
  .stage {
    width: 1200px; height: 875px;
    display: flex; align-items: center; justify-content: center; gap: 44px;
  }
  .card {
    width: 540px; height: 309px;
    border-radius: 22px;
    position: relative;
    overflow: hidden;
    box-shadow: 0 18px 40px rgba(0,0,0,.45);
  }
  .ribbons {
    position: absolute; inset: 0;
    width: 100%; height: 100%;
    pointer-events: none;
  }
  .card-front {
    background: var(--front-bg);
    display: flex; align-items: center; justify-content: center;
  }
  .wordmark {
    position: relative;
    display: flex; align-items: center; gap: 12px;
    font-weight: 600; letter-spacing: .5px;
    white-space: nowrap;
  }
  .wordmark-dot { width: 14px; height: 14px; border-radius: 50%; flex: none; }
  .card-front .wordmark { font-size: 46px; color: var(--front-ink); margin-top: -20px; }
  .card-front .wordmark-dot { background: var(--front-ink); }

  .card-back {
    background: linear-gradient(160deg, var(--back-bg-top), var(--back-bg-bottom));
    display: flex; align-items: center;
    padding: 0 34px 36px 40px;
  }
  .card-back .wordmark { font-size: 30px; color: var(--navy); width: 200px; }
  .card-back .wordmark-dot { background: var(--teal); width: 10px; height: 10px; }
  .divider {
    position: relative;
    width: 1px; height: 150px; background: var(--divider);
    margin: 0 26px 0 16px; flex: none;
  }
  .contact { position: relative; color: var(--body-ink); }
  .contact-name {
    font-weight: 600; font-size: 19px; color: var(--navy);
    letter-spacing: .4px; line-height: 1.1;
  }
  .contact-title { font-size: 12.5px; margin-bottom: 10px; }
  .contact-address { font-size: 12.5px; line-height: 1.35; margin-bottom: 12px; }
  .contact-list { list-style: none; font-size: 12.5px; }
  .contact-list li { display: flex; align-items: center; gap: 8px; line-height: 1.5; }
  .contact-list svg { width: 11px; height: 11px; fill: var(--teal); flex: none; }
</style>
</head>
<body>
<main class="stage">
  <section class="card card-front" aria-label="Card front">
    <svg class="ribbons" viewBox="0 0 540 309" preserveAspectRatio="none" aria-hidden="true">
      <path d="M0 262 C150 228 340 292 540 240 L540 309 L0 309 Z" fill="#5a6d84"/>
      <path d="M0 276 C160 246 350 304 540 258 L540 266 C350 312 160 256 0 286 Z" fill="var(--teal-soft)" opacity=".7"/>
    </svg>
    <div class="wordmark"><span class="wordmark-dot"></span>KX7 Supply</div>
  </section>

  <section class="card card-back" aria-label="Card back">
    <svg class="ribbons" viewBox="0 0 540 309" preserveAspectRatio="none" aria-hidden="true">
      <path d="M0 268 C150 234 340 296 540 246 L540 309 L0 309 Z" fill="var(--navy)"/>
      <path d="M0 252 C160 220 350 282 540 230 L540 248 C340 298 150 236 0 270 Z" fill="var(--teal)"/>
      <path d="M0 240 C170 212 360 268 540 218 L540 226 C350 276 160 222 0 248 Z" fill="var(--teal-soft)"/>
      <path d="M420 0 C470 30 500 60 540 70 L540 0 Z" fill="var(--teal)" opacity=".18"/>
    </svg>
    <div class="wordmark"><span class="wordmark-dot"></span>KX7 Supply</div>
    <div class="divider"></div>
    <div class="contact">
      <p class="contact-name">DANIEL REYES</p>
      <p class="contact-title">General Manager</p>
      <p class="contact-address">42 Harbor Point Drive<br>Lakeview, OH 44102 USA</p>
      <ul class="contact-list">
        <li><svg viewBox="0 0 24 24"><path d="M6.6 10.8a15.1 15.1 0 0 0 6.6 6.6l2.2-2.2a1 1 0 0 1 1-.25 11.4 11.4 0 0 0 3.6.57 1 1 0 0 1 1 1V20a1 1 0 0 1-1 1A17 17 0 0 1 3 4a1 1 0 0 1 1-1h3.5a1 1 0 0 1 1 1c0 1.250.2 2.450.57 3.57a1 1 0 0 1-.25 1z"/></svg>+1.555.010.482</li>
        <li><svg viewBox="0 0 24 24"><path d="M2 5h20v14H2zm2 2v.5l8 5 8-5V7l-8 5z"/></svg>name@kx7supply.com</li>
        <li><svg viewBox="0 0 24 24"><path d="M12 2a10 10 0 1 0 0 20 10 10 0 0 0 0-20zm6.9 9h-3a15 15 0 0 0-1.4-6A8 8 0 0 1 18.9 11zM12 4c.9 1.2 1.8 3.5 2 7h-4c.2-3.5 1.1-5.8 2-7zM9.5 5a15 15 0 0 0-1.4 6h-3A8 8 0 0 1 9.5 5zm-4.4 8h3a15 15 0 0 0 1.4 6 8 8 0 0 1-4.4-6zM12 20c-.9-1.2-1.8-3.5-2-7h4c-.2 3.5-1.1 5.8-2 7zm2.5-1a15 15 0 0 0 1.4-6h3a8 8 0 0 1-4.4 6z"/></svg>www.kx7supply.com</li>
      </ul>
    </div>
  </section>
</main>
</body>
</html>
```